Car Accessory Flyer to advertise parking sensors, heated seats, car security

I'm looking to have a double sided flyer made that will be distributed locally to advertise heated seats and parking sensors on one side. And trackers and Tarvo immobilisers on the other. Our website is www.dernilo.co.uk
I'm hoping its possible to use wording and pictures from our website.

Target Market(s)
Car owners looking to upgrade their car to have parking sensors or heated seats.
Luxury car owners who are worried about their vehicle being stolen.
Industry/Entity Type
Automotive
Requirements
Must have
- Pictures
Our website, phone number and address
Flyer will be A5 double sided
Nice to have
- A design similar to our website

```html
<!DOCTYPE html>
<html lang="en">
<head>
<meta charset="utf-8">
<title>Dernilo – Car Accessory Flyer</title>
<link rel="stylesheet" href="https://fonts.googleapis.com/css2?family=Abel&display=swap">
<style>
  :root {
    --backdrop: #dccfd2;
    --paper: #f3f3f2;
    --band: #575757;
    --ink: #2f2f2f;
    --ink-soft: #3c3c3c;
    --rule: #4a4a4a;
    --on-band: #ffffff;
    --photo-car: #4a4d52;
    --photo-car-light: #8d8f93;
    --photo-seat: #3a3a3c;
    --photo-seat-light: #9a958c;
    --shot-map: #3d4d5e;
    --shot-map-light: #7d8a8c;
    --promo-dark: #2a3038;
    --promo-light: #5b6b7a;
    --street-map: #dfe6dc;
    --street-map-green: #b9d6ab;
  }
  * { box-sizing: border-box; margin: 0; padding: 0; }
  html, body { width: 1200px; height: 900px; overflow: hidden; }
  body {
    background: var(--backdrop);
    font-family: "Abel", "Arial Narrow", sans-serif;
    color: var(--ink);
    position: relative;
  }
  .flyer {
    position: absolute;
    top: 50px;
    width: 566px;
    height: 800px;
    background: var(--paper);
    box-shadow: 0 4px 14px rgba(80, 50, 60, 0.18);
    overflow: hidden;
  }
  .flyer--front { left: 20px; }
  .flyer--back { left: 614px; }

  .hero-band { position: absolute; left: 0; top: 0; width: 566px; height: 180px; }
  .hero-title {
    position: absolute;
    color: var(--on-band);
    font-size: 38px;
    line-height: 1;
    letter-spacing: 0.5px;
    white-space: nowrap;
  }
  .hero-title--one { left: 151px; top: 32px; }
  .hero-title--two { left: 232px; top: 78px; }
  .hero-title--three { left: 307px; top: 126px; }

  .section-title {
    position: absolute;
    font-size: 31px;
    line-height: 1;
    color: var(--ink);
    letter-spacing: 0.3px;
    white-space: nowrap;
  }
  .section-rule {
    position: absolute;
    height: 1.5px;
    background: var(--rule);
  }
  .section-copy {
    position: absolute;
    font-size: 12.6px;
    line-height: 16.4px;
    color: var(--ink-soft);
  }
  .section-copy--justified { text-align: justify; }
  .price-note {
    position: absolute;
    font-size: 13px;
    line-height: 17px;
    font-style: italic;
    text-align: center;
    color: var(--ink-soft);
  }
  .photo { position: absolute; }
  .photo--car { background: linear-gradient(170deg, var(--photo-car-light), var(--photo-car) 55%, #2d2f33); }
  .photo--seat { background: linear-gradient(135deg, var(--photo-seat-light), var(--photo-seat) 50%, #1f1f21); }
  .photo--tracking-app { background: linear-gradient(160deg, var(--shot-map-light), var(--shot-map)); border: 1.5px solid #2a3f7a; }
  .photo--immobiliser-promo { background: linear-gradient(135deg, var(--promo-light), var(--promo-dark) 60%); }
  .photo--street-map { background: linear-gradient(150deg, var(--street-map), var(--street-map-green)); }

  .footer-band {
    position: absolute;
    left: 0; bottom: 0;
    width: 566px;
    height: 75px;
    background: var(--band);
    color: var(--on-band);
  }
  .brand-name {
    position: absolute;
    left: 48px;
    top: 22px;
    font-size: 30px;
    line-height: 1;
    letter-spacing: 1px;
    color: var(--on-band);
  }
  .footer-contact {
    position: absolute;
    right: 34px;
    top: 17px;
    text-align: right;
    font-size: 16px;
    line-height: 19px;
  }
  .address-line {
    position: absolute;
    left: 0; width: 566px;
    top: 676px;
    text-align: center;
    font-size: 13px;
    line-height: 17px;
    font-style: italic;
    color: var(--ink-soft);
  }
</style>
</head>
<body>

<section class="flyer flyer--front">
  <svg class="hero-band" viewBox="0 0 566 180" aria-hidden="true">
    <polygon points="0,0 566,0 566,180 286,180 255,130 160,130 124,84 0,84" fill="var(--band)"/>
  </svg>
  <h1 class="hero-title hero-title--one">PARKING SENSORS</h1>
  <p class="hero-title hero-title--two">HEATED SEATS</p>
  <p class="hero-title hero-title--three">CAR SECURITY</p>

  <h2 class="section-title" style="left:48px; top:215px;">PARKING SENSORS</h2>
  <div class="section-rule" style="left:48px; top:250px; width:472px;"></div>
  <p class="section-copy section-copy--justified" style="left:48px; top:262px; width:224px;">
    Make parking a breeze by adding parking sensors to your car.<br>
    We offer a range of different options, our preferred option is flush mount OEM style but have a<br>
    solution for all vehicles<br>
    Our two most poplar options are the standard “mount from the outside” type and the flush OEM<br>
    style sensors, both can be colour coded.
  </p>
  <div class="photo photo--car" style="left:377px; top:264px; width:144px; height:144px;" role="img" aria-label="Photo of a dark hatchback seen from the rear in the workshop, fitted with parking sensors"></div>
  <p class="price-note" style="left:377px; top:416px; width:144px;">From<br>£190</p>

  <h2 class="section-title" style="left:48px; top:475px;">HEATED SEATS</h2>
  <div class="section-rule" style="left:48px; top:510px; width:472px;"></div>
  <p class="section-copy" style="left:49px; top:521px; width:230px;">
    Give yourself the luxury of heated seats.<br>
    We take your ordinary seats and convert them to heated.<br>
    From the outside they will look completely standard, we install heating elements to the base and<br>
    back between the seat cover and foam, with the addition of a conveniently placed switch with the<br>
    option of High heat, low heat or off.<br>
    Suitable for both leather and fabric seats.
  </p>
  <div class="photo photo--seat" style="left:377px; top:522px; width:144px; height:119px;" role="img" aria-label="Close-up photo of a heated seat switch fitted beside a car seat"></div>
  <p class="price-note" style="left:357px; top:650px; width:184px;">£350<br>for a pair of front seats</p>

  <footer class="footer-band">
    <span class="brand-name">DERNILO</span>
    <p class="footer-contact">www.dernilo.co.uk<br>call us at 0131 555 0192</p>
  </footer>
</section>

<section class="flyer flyer--back">
  <h2 class="section-title" style="left:41px; top:42px;">TRACKERS</h2>
  <div class="section-rule" style="left:41px; top:80px; width:477px;"></div>
  <p class="section-copy section-copy--justified" style="left:47px; top:91px; width:230px;">
    Are you worried about your vehicle being stolen? An insurance approved tracker greatly improves<br>
    the chance of getting it back. Tracking via and App or web browser. .
  </p>
  <div class="photo photo--tracking-app" style="left:339px; top:92px; width:182px; height:103px;" role="img" aria-label="Screenshot of the tracking app showing a satellite map with a vehicle location"></div>
  <p class="price-note" style="left:330px; top:206px; width:200px;">From as little as £399 inc the first year subscription then £100 thereafter</p>

  <h2 class="section-title" style="left:47px; top:289px;">VELTRAC TARVO</h2>
  <div class="section-rule" style="left:47px; top:328px; width:477px;"></div>
  <p class="section-copy section-copy--justified" style="left:47px; top:338px; width:230px;">
    Veltrac Tarvo II<br>
    The Veltrac Tarvo II helps protect your car against keyless entry theft. Even if a thief has your<br>
    keys or is using a relay device to program a new key your car will not start unless your unique<br>
    code has been entered using a combination of buttons on your dash or steering wheel.
  </p>
  <div class="photo photo--immobiliser-promo" style="left:338px; top:340px; width:184px; height:103px;" role="img" aria-label="Promotional graphic for the Tarvo II immobiliser with a hand pressing security icons"></div>
  <p class="price-note" style="left:380px; top:451px; width:100px;">From<br>£449</p>

  <div class="photo photo--street-map" style="left:192px; top:522px; width:186px; height:137px;" role="img" aria-label="Street map of south-west Edinburgh with a pin marking the Dernilo workshop"></div>
  <p class="address-line">Dernilo, 14 Harlow Brae Yards, Edinburgh, Scotland,<br>EH12 4QN, United Kingdom</p>

  <footer class="footer-band">
    <span class="brand-name">DERNILO</span>
    <p class="footer-contact">www.dernilo.co.uk<br>call us at 0131 555 0192</p>
  </footer>
</section>

</body>
</html>
```